Midwife Poster Ad

I need a poster to go on a wall in my clinic which is in a medical centre shared by doctors and other health professionals. I am a self-employed midwife in New Zealand. I hope for this poster to catch some of the many women who come into the medical centre to have pregnancy tests, see a doctor, or use the pregnancy yoga/pilates services also offered. It will be going on a wall with a bunch of other brochures and ads, so obviously I would like it to stand out and grab their attention as they walk in or out of the centre.

I have attached a few of the images that I currently use in my business cards and brochures. I would like my portrait to feature somewhere on the poster, but does not need to be central. The other images can be used if they work with the design, but are not essential. I would like the poster to include at least one image of a new baby or a pregnant woman/couple.

I would also like a small business card-sized space at the bottom where I can attach a card-holder. I would like the website address to stand out.

The poster should be colourful and communicate the excitement of a new pregnancy.

Target Market(s)

Pregnant women, mothers

Industry/Entity Type

Small Business

Requirements
Must have
• The poster needs to include the following text:
EXPECTING A BABY?
Midwife available here!
Rosalind Forde LMC Midwife
Clinics run from Harbour Physio & Pilates
Free pregnancy testing
www.brookvalemidwife.co.nz
0227351846

```html
<!DOCTYPE html>
<html lang="en">
<head>
<meta charset="utf-8">
<title>Expecting a baby? – Midwife Poster</title>
<link rel="stylesheet" href="https://fonts.googleapis.com/css2?family=Sniglet:wght@400;800&family=Questrial&display=swap">
<style>
  :root {
    --paper: #ffffff;
    --violet: #6a45f2;
    --violet-deep: #5a36e6;
    --violet-soft: #a796f7;
    --violet-mist: #c9bffb;
    --cyan: #2de6f2;
    --ink: #111111;
    --skin-light: #f3d6cc;
    --skin-mid: #e3a99c;
    --skin-deep: #c9877c;
    --portrait-light: #e8cbb8;
    --portrait-dark: #2a2a38;
  }
  * { margin: 0; padding: 0; box-sizing: border-box; }
  html, body {
    width: 1000px; height: 1200px; overflow: hidden;
    background: var(--paper);
  }
  .poster {
    position: relative;
    width: 1000px; height: 1200px;
    background: var(--paper);
    overflow: hidden;
    font-family: "Questrial", "Century Gothic", sans-serif;
  }
  .baby-photo {
    position: absolute;
    left: 320px; top: 10px;
    width: 580px; height: 780px;
    border-radius: 260px 0 0 40px;
    background:
      radial-gradient(ellipse 55% 40% at 50% 28%, var(--skin-light), transparent 75%),
      linear-gradient(160deg, var(--skin-mid) 0%, var(--skin-deep) 40%, var(--skin-light) 80%);
  }
  .headline-band {
    position: absolute;
    left: 320px; top: 450px;
    width: 580px; height: 268px;
    background: rgba(255, 255, 255, 0.62);
  }
  .headline {
    position: absolute;
    right: 128px; top: 462px;
    font-family: "Sniglet", "Arial Rounded MT Bold", "Arial Black", sans-serif;
    font-weight: 800;
    color: var(--violet);
    font-size: 112px;
    line-height: 122px;
    text-align: right;
    white-space: nowrap;
  }
  .portrait {
    position: absolute;
    left: 57px; top: 712px;
    width: 272px; height: 300px;
    border-radius: 120px 120px 0 0;
    background: linear-gradient(180deg, var(--portrait-light) 0%, var(--portrait-light) 62%, var(--portrait-dark) 78%);
  }
  .waves {
    position: absolute;
    left: 0; top: 900px;
    width: 1000px; height: 130px;
  }
  .tagline {
    position: absolute;
    left: 287px; top: 776px;
    font-size: 51px;
    color: var(--cyan);
    white-space: nowrap;
  }
  .details {
    position: absolute;
    left: 320px; top: 840px;
    list-style: none;
    color: var(--ink);
    font-size: 26px;
    line-height: 37px;
    white-space: nowrap;
  }
  .details .midwife-name { font-weight: 700; -webkit-text-stroke: 0.4px var(--ink); }
  .contact-bar {
    position: absolute;
    left: 57px; top: 1020px;
    width: 843px; height: 170px;
    background: var(--violet);
  }
  .website, .phone {
    position: absolute;
    left: 50px;
    color: var(--paper);
    white-space: nowrap;
  }
  .website { top: 36px; font-size: 33px; font-weight: 700; -webkit-text-stroke: 0.8px var(--paper); }
  .phone { top: 84px; font-size: 39px; letter-spacing: 1px; -webkit-text-stroke: 0.5px var(--paper); }
  .card-holder {
    position: absolute;
    left: 585px; top: 29px;
    width: 169px; height: 110px;
    border: 1px solid #3b1fb0;
    background: var(--violet-deep);
  }
</style>
</head>
<body>
  <main class="poster">
    <div class="baby-photo" role="img" aria-label="Photograph of a sleeping newborn baby resting on a parent's chest"></div>
    <div class="headline-band"></div>
    <h1 class="headline">Expecting<br>a baby?</h1>

    <div class="portrait" role="img" aria-label="Portrait photograph of the midwife, smiling"></div>

    <svg class="waves" viewBox="0 0 1000 130" aria-hidden="true">
      <path d="M57 80 C 250 40, 420 110, 620 70 S 850 20, 900 28 L 900 130 L 57 130 Z" fill="var(--violet-mist)" opacity="0.8"/>
      <path d="M57 95 C 260 70, 430 120, 640 90 S 860 50, 900 60 L 900 130 L 57 130 Z" fill="var(--violet-soft)" opacity="0.85"/>
      <path d="M57 112 C 280 95, 460 128, 660 110 S 870 90, 900 95 L 900 130 L 57 130 Z" fill="var(--violet)"/>
    </svg>

    <p class="tagline">Midwife available here!</p>
    <ul class="details">
      <li class="midwife-name">Rosalind Forde LMC Midwife</li>
      <li>Clinics run from Harbour Physio &amp; Pilates</li>
      <li>Free pregnancy testing</li>
    </ul>

    <footer class="contact-bar">
      <p class="website">www.brookvalemidwife.co.nz</p>
      <p class="phone">0227351846</p>
      <div class="card-holder" aria-label="Space for business card holder"></div>
    </footer>
  </main>
</body>
</html>
```